Tolvex Engineers: Why you should hire us keepsake

New design. Open to plastic cards. We are an engineering firm that designs cell phone towers and commercial buildings. Please check out our website www.tolvexgrp.com for more details. We want people to remember our card and for it to be useful if possible. We want the same look and feel on these cards to be translated to other marketing material we may need such as brochures.

Target Market(s)

Architects, Developers and Telecommunication Carriers

Industry/Entity Type

Engineering

Contact Information for Business Card

Card with our company colors, logo, and innovative design with elements related to our industry.

Font styles to use
Sans Serif

Colors
9bcb3c
abd036
0255a3

Requirements
Must have
• Sleek and hip design
Nice to have
• Bright lime green and navy coloring that pops with an innovative design.
Should not have
• A basic and boring design

```html
<!DOCTYPE html>
<html lang="en">
<head>
<meta charset="utf-8">
<title>Tolvex Engineers Business Card</title>
<link href="https://fonts.googleapis.com/css2?family=Arimo:wght@400;700&display=swap" rel="stylesheet">
<style>
  :root {
    --navy-deep: #021a4a;
    --navy-soft: #3b4f74;
    --lime: #1fd11f;
    --lime-text: #2ee02e;
    --frost: #e6eaec;
    --frost-edge: #d6dcdf;
    --ink-navy: #0b1f4d;
    --ink-grey: #2b3340;
    --white: #ffffff;
    --stage: #eef1f2;
  }
  html, body {
    margin: 0;
    padding: 0;
    width: 1200px;
    height: 970px;
    overflow: hidden;
    background: radial-gradient(ellipse at center, #f8fafa 0%, var(--stage) 70%, #e2e6e8 100%);
    font-family: "Arimo", Arial, sans-serif;
  }
  .business-card {
    position: absolute;
    left: 100px;
    top: 207px;
    width: 1000px;
    height: 556px;
    border-radius: 44px;
    overflow: hidden;
    display: flex;
    box-shadow: 0 18px 40px rgba(20, 30, 50, 0.18);
  }
  .card-contact {
    position: relative;
    width: 517px;
    height: 100%;
    background: linear-gradient(135deg, var(--navy-soft) 0%, #223763 45%, var(--navy-deep) 75%, #2c406a 100%);
    color: var(--white);
  }
  .divider {
    position: relative;
    width: 9px;
    height: 100%;
    background: var(--lime);
  }
  .divider-notch {
    position: absolute;
    left: -24px;
    top: 94px;
    width: 24px;
    height: 84px;
  }
  .card-brand {
    position: relative;
    flex: 1;
    background: linear-gradient(160deg, #f1f3f4 0%, var(--frost) 55%, var(--frost-edge) 100%);
  }
  .person-name {
    position: absolute;
    right: 77px;
    top: 114px;
    margin: 0;
    font-size: 29px;
    font-weight: 700;
    letter-spacing: 0.2px;
    text-transform: uppercase;
  }
  .firm-details {
    position: absolute;
    right: 77px;
    top: 289px;
    text-align: right;
    font-size: 21px;
    line-height: 29px;
  }
  .discipline {
    color: var(--lime-text);
    text-transform: uppercase;
  }
  .contact-list {
    position: absolute;
    right: 65px;
    top: 414px;
    margin: 0;
    padding: 0;
    list-style: none;
    font-size: 21px;
    line-height: 30px;
  }
  .contact-list li {
    display: flex;
    justify-content: flex-end;
    align-items: center;
    gap: 12px;
  }
  .contact-icon {
    width: 22px;
    height: 22px;
    flex: none;
  }
  .brand-name {
    position: absolute;
    left: 70px;
    top: 78px;
    margin: 0;
    color: var(--lime);
    font-size: 54px;
    font-weight: 700;
    line-height: 58px;
    text-transform: uppercase;
  }
  .website {
    position: absolute;
    left: 0;
    right: 0;
    top: 478px;
    text-align: center;
    font-size: 21px;
    letter-spacing: 9px;
    color: var(--ink-grey);
  }
  .website strong {
    color: var(--ink-navy);
    font-weight: 700;
  }
</style>
</head>
<body>
  <article class="business-card">
    <section class="card-contact">
      <h1 class="person-name">Dana Reyes Holt</h1>
      <div class="firm-details">
        <div class="discipline">Multi-Discipline Engineering</div>
        <div>2400 Birchline Pkwy</div>
        <div>Suite 310 Alderton, GA 30190</div>
      </div>
      <ul class="contact-list">
        <li>555.014.2387
          <svg class="contact-icon" viewBox="0 0 22 22"><rect x="6" y="1.5" width="11" height="19" rx="2" fill="none" stroke="#1fd11f" stroke-width="2"/><line x1="9.5" y1="17" x2="13.5" y2="17" stroke="#1fd11f" stroke-width="1.6"/></svg>
        </li>
        <li>555.018.6642
          <svg class="contact-icon" viewBox="0 0 22 22"><path d="M6 3 L9 3 L10.5 7.5 L8.5 9 C9.5 11.5 11 13 13.5 14 L15 12 L19 13.5 L19 17 C19 18 18 19 17 19 C10 18.5 4 12.5 3.5 5.5 C3.5 4 4.5 3 6 3 Z" fill="#1fd11f"/></svg>
        </li>
        <li>dholt@tolvexgrp.com
          <svg class="contact-icon" viewBox="0 0 22 22"><rect x="1.5" y="5" width="19" height="13" fill="#1fd11f"/><path d="M1.5 5 L11 12.5 L20.5 5" fill="none" stroke="#223763" stroke-width="1.5"/></svg>
        </li>
      </ul>
    </section>
    <div class="divider">
      <svg class="divider-notch" viewBox="0 0 24 84" aria-hidden="true"><polygon points="24,0 0,42 24,84" fill="#1fd11f"/></svg>
    </div>
    <section class="card-brand">
      <h2 class="brand-name">Tolvex<br>Engineers</h2>
      <div class="website">www.<strong>tolvexgrp</strong>.com</div>
    </section>
  </article>
</body>
</html>
```